Personal Training

The name of my company is Heron Fitness. I am looking for a design that will feature the 8 components I am utilizing in my workouts (strength, flexibility, agility, core, power, balance, cardiovacular, speed) and represent the spider. It is not essesstial to have a spider for my logo but would be nice. If a spider is used please do not use a logo like Gullwoman, a tarantula, or anything scary involving a spider (I have female clients who would get scared) lol
If you need me to provide more information please let me know. Feel free to check my website for ideas but ignore the pictures on my site as those are not pictures of me or clients
Thank you in advance!

Industry/Entity Type

Fitness

Contact Information for Business Card

Mark Delaney
Company Name: Heron Fitness
Tag line: 8 components to a better you
Website: hernfit4.example
Email: mark@hernfit4.example
Cell: 555-314-2086

CQBL Certified Personal Trainer
CPR AED National Pulse Federation
B.A. Exercise Physiology W.K.R., 2004

```html
<!DOCTYPE html>
<html lang="en">
<head>
<meta charset="utf-8">
<title>Heron Fitness – Business Card</title>
<link rel="stylesheet" href="https://fonts.googleapis.com/css2?family=Source+Sans+3:wght@400;600;700&display=swap">
<style>
  :root {
    --backdrop: #e6e4e1;
    --card-black: #161616;
    --brand-red: #d94141;
    --band-grey: #b9b9b9;
    --panel-white: #f3f3f3;
    --light-text: #dedede;
    --dark-text: #1b1b1b;
  }
  html, body {
    margin: 0;
    padding: 0;
    width: 1200px;
    height: 738px;
    overflow: hidden;
    background: var(--backdrop);
  }
  .canvas {
    width: 1200px;
    height: 738px;
    display: flex;
    align-items: center;
    justify-content: center;
  }
  .business-card {
    width: 1100px;
    height: 629px;
    display: block;
    box-shadow: 0 4px 14px rgba(0,0,0,0.25);
    font-family: "Source Sans 3", sans-serif;
  }
  .card-base { fill: var(--card-black); }
  .swoosh-red { fill: var(--brand-red); }
  .swoosh-line-black { fill: none; stroke: var(--card-black); stroke-width: 7; stroke-linecap: round; }
  .swoosh-line-grey { fill: none; stroke: var(--band-grey); stroke-width: 7; stroke-linecap: round; }
  .info-panel { fill: var(--panel-white); }
  .brand-dot { fill: var(--brand-red); }
  .brand-name { fill: var(--light-text); font-weight: 700; font-size: 48px; }
  .person-name { fill: var(--light-text); font-weight: 600; font-size: 44px; }
  .person-role { fill: var(--brand-red); font-weight: 400; font-size: 30px; }
  .credentials { fill: var(--dark-text); font-weight: 400; font-size: 26px; }
  .contact-heading { fill: var(--brand-red); font-weight: 700; font-size: 32px; }
  .contact-line { fill: var(--dark-text); font-weight: 400; font-size: 25px; }
  .contact-label { fill: var(--brand-red); font-weight: 700; }
  .contact-divider { stroke: var(--brand-red); stroke-width: 2; }
</style>
</head>
<body>
<main class="canvas">
  <svg class="business-card" viewBox="0 0 1100 629" xmlns="http://www.w3.org/2000/svg" aria-label="Heron Fitness business card for Mark Delaney">
    <rect class="card-base" x="0" y="0" width="1100" height="629"/>

    <!-- swoosh band -->
    <path class="swoosh-red" d="M192 629 C176 450 300 310 700 298 C880 292 1000 300 1100 304 L1100 336 C1000 330 880 322 700 328 C320 330 210 420 236 629 Z"/>
    <path class="swoosh-line-black" d="M206 629 C196 520 236 450 320 400"/>
    <path class="swoosh-line-grey" d="M214 629 C205 525 244 456 326 404"/>
    <path class="swoosh-line-black" d="M223 629 C214 530 252 462 330 410"/>

    <!-- white info panel -->
    <path class="info-panel" d="M236 629 C210 420 320 330 700 328 C880 322 1000 330 1100 336 L1100 629 Z"/>

    <!-- brand -->
    <circle class="brand-dot" cx="107" cy="145" r="64"/>
    <text class="brand-name" x="196" y="162">Heron Fitness</text>

    <!-- person -->
    <text class="person-name" x="1021" y="167" text-anchor="end">Mark Delaney</text>
    <text class="person-role" x="1021" y="218" text-anchor="end">Personal Trainer</text>

    <!-- credentials -->
    <text class="credentials" x="700" y="392" text-anchor="middle">Personal Trainer CPR AED National Pulse</text>
    <text class="credentials" x="700" y="432" text-anchor="middle">Federation B.A. Exercise Physiology W.K.R., 2004</text>

    <!-- contact -->
    <text class="contact-heading" x="691" y="488" text-anchor="middle">Contact details</text>
    <line class="contact-divider" x1="685" y1="520" x2="685" y2="620"/>

    <text class="contact-line" x="662" y="546" text-anchor="end"><tspan class="contact-label">Cell:</tspan> 555-314-2086</text>
    <text class="contact-line" x="662" y="586" text-anchor="end">CQBL Certified</text>

    <text class="contact-line" x="710" y="546"><tspan class="contact-label">Email:</tspan> mark@hernfit4.example</text>
    <text class="contact-line" x="710" y="586"><tspan class="contact-label">Website:</tspan> hernfit4.example</text>
  </svg>
</main>
</body>
</html>
```